Brochure for an engineering consultancy

We need a brochure design for our engineering consulting business. We basically deal with ground-related works (i.e. foundations, drill rigs, excavators, road embankments...etc). We have two main aspects of our work. They are as following:
1- Design Services: this is related to office work like calculations, drawings and engineering tools and software.
2- Construction Support Services: outdoor work where we go to construction sites and supervise and watch the projects being built onsite.
3- Ground investigations where we test the ground to know how strong it is for building
Please have a look at our website www.pelvarco.com.au for an idea of whet we do. You can use materials from the website for this brochure only.
We are after a simple but yet very attractive brochure to suit both office-minded people and construction-minded people. We have prepared some symbols that we would like to use on the brochure in addition to the attached photos. Those are symbols we created so please, do not use them on other projects.
The winning design the one that would succeed in reflecting professionalism, trustworthiness and helpfulness. Please remember, we make money out of engineering ADVICE and KNOWLEDGE.
Our logo is also attached. Include blue colour please. Also A4 single fold please.
Target Market(s)
construction companies, buildings developers and engineering consultants
Industry/Entity Type
Business
Requirements
Must have
- all 3 of our services in this order
- 1- Construction support services
- 2- Ground investigation services
- 3- Design services
Should not have
- Excessive presence of excavators and earthmoving machines. From our experience brochure designers think we are an excavator hiring company or that we are earthmoving contractors. We are not. We are an engineering consultant

```html
<!DOCTYPE html>
<html lang="en">
<head>
<meta charset="utf-8">
<title>Pelvarco Brochure Spread</title>
<link href="https://fonts.googleapis.com/css2?family=Roboto:wght@400;500;700&family=Roboto+Condensed:wght@700&display=swap" rel="stylesheet">
<style>
  :root {
    --backdrop: #6e7075;
    --paper: #ffffff;
    --brand-blue: #1a6fc0;
    --heading-blue: #1a5ea8;
    --text: #3c3c3c;
    --rule-grey: #a9a9a9;
    --art-grey: #e9eaec;
  }
  * { box-sizing: border-box; margin: 0; padding: 0; }
  html, body { width: 1200px; height: 879px; overflow: hidden; background: var(--backdrop); }
  body { position: relative; font-family: "Roboto", Arial, sans-serif; color: var(--text); }

  .page { position: absolute; top: 69px; width: 523px; height: 740px; background: var(--paper); overflow: hidden; }
  .page--left { left: 77px; }
  .page--right { left: 600px; }

  .top-band { position: absolute; top: 28px; left: 0; width: 340px; height: 22px; background: var(--brand-blue); }

  .brand { position: absolute; top: 24px; right: 14px; display: flex; align-items: center; gap: 7px; }
  .brand__mark { width: 26px; height: 26px; background: var(--brand-blue); }
  .brand__name { font-family: "Roboto", Arial, sans-serif; font-weight: 500; font-size: 24px; letter-spacing: 1.5px; color: var(--brand-blue); }

  .section-title { position: absolute; top: 67px; left: 31px; font-family: "Roboto Condensed", Arial, sans-serif; font-weight: 700; font-size: 23.5px; color: var(--heading-blue); white-space: nowrap; }

  .intro { position: absolute; left: 31px; width: 470px; font-size: 9.8px; line-height: 12.7px; }
  .services { position: absolute; left: 31px; width: 470px; list-style: none; font-size: 9.8px; line-height: 12.7px; }
  .services li { position: relative; padding-left: 15px; }
  .services li::before { content: ""; position: absolute; left: 0; top: 3px; width: 7px; height: 7px; border-radius: 50%; background: var(--brand-blue); }
  .services .term { color: var(--brand-blue); }

  .section--support .intro { top: 116px; }
  .section--support .services { top: 180px; }
  .section--support .services li { margin-bottom: 9px; }

  .section--design .intro { top: 119px; font-weight: 500; }
  .section--design .services { top: 140px; }
  .section--design .services li { margin-bottom: 4.5px; }

  .visual { position: absolute; width: 118px; height: 118px; border-radius: 50%; }
  .visual--diagram { background: var(--art-grey); border: 2px solid #222; }

  .footer-rule { position: absolute; bottom: 21px; left: 0; width: 467px; height: 7px; background: var(--rule-grey); }
  .page-number { position: absolute; bottom: 16px; left: 467px; width: 37px; height: 22px; background: var(--brand-blue); color: #fff; font-size: 11px; font-weight: 500; display: flex; align-items: center; justify-content: center; }
</style>
</head>
<body>

<section class="page page--left section--support">
  <div class="top-band"></div>
  <div class="brand"><span class="brand__mark"></span><span class="brand__name">PELVARCO</span></div>
  <h2 class="section-title">1. Construction Support and Site Inspections</h2>
  <p class="intro">We provide construction support through site inspections and production of inspection reports, on-site designs and changes to existing designs if required. We understand that designs are sometimes generic and we customise those designs to suit you project and provide you with achievable and safer results. Our Construction Support services include:</p>
  <ul class="services">
    <li>Piling Inspections: to confirm the required rock socket and bearing capacity as well as the pile toe cleanness have been achieved. We provide inspection reports and sign-offs at completion for ordinary and CFA piling</li>
    <li>Piling/Working Platforms: on-the-spot design of piling platform after application of light ground testing. Geogrid are specified sometimes if required (based on ground condition)<br>Excavation Face Inspections: for application of shotcrete in basements and to confirm saw cut faces are free of seams</li>
    <li>Slope Stability Assessments / Inspection: for cuts in soil/rock or built up embankments. Assessment is carried out to confirm the extent of required battering during excavations of open cuts or trenches; or for embankments</li>
    <li>Anchoring Inspections: to sign off on anchors installation, stressing, distressing and removal/grouting<br>Foundation Inspections: to assess the bearing capacity of the founding materials<br>Proof Rolling: and soft spot identification during the earthworks preparation for pavement/slab on ground construction</li>
  </ul>
  <div class="visual" style="left:70px;top:419px;background:radial-gradient(circle at 45% 40%,#b9a48f,#6f5a48)" role="img" aria-label="Site photo: rock socket spoil from pile drilling"></div>
  <div class="visual" style="left:202px;top:419px;background:linear-gradient(180deg,#8fb2d6 0%,#b8b4a8 40%,#6d6a62 100%)" role="img" aria-label="Site photo: basement shoring wall with shotcrete panels"></div>
  <div class="visual" style="left:333px;top:419px;background:linear-gradient(180deg,#c7cbd0 0%,#c9a36f 45%,#a88456 100%)" role="img" aria-label="Site photo: open cut excavation face"></div>
  <div class="visual" style="left:70px;top:550px;background:radial-gradient(circle at 50% 45%,#d8642e,#7a5a3c)" role="img" aria-label="Site photo: roller during proof rolling"></div>
  <div class="visual" style="left:202px;top:550px;background:radial-gradient(circle at 50% 50%,#bfc2c4,#5c6064)" role="img" aria-label="Site photo: excavated rock face inspection"></div>
  <div class="visual" style="left:333px;top:550px;background:linear-gradient(180deg,#7f9a6a 0%,#a08c6a 55%,#c2a47c 100%)" role="img" aria-label="Site photo: piling platform earthworks"></div>
  <div class="footer-rule"></div>
  <div class="page-number">02</div>
</section>

<section class="page page--right section--design">
  <div class="top-band"></div>
  <div class="brand"><span class="brand__mark"></span><span class="brand__name">PELVARCO</span></div>
  <h2 class="section-title">3. Tender and Detailed Design</h2>
  <p class="intro">We provide tender design as well as detailed design for within the following areas:</p>
  <ul class="services">
    <li><span class="term">Pile Foundations:</span> we design piles for the most complex site condition and loading conditions, including cast in place and driven concrete and steel piles. We proudly designed the largest size concrete piles with 2.8m diameter for some bridges over rivers in NSW.</li>
    <li><span class="term">Shoring Walls:</span> for rail and transport corridors as well as buildings' basements including concrete, steel and composite soldier pile wall, contiguous pile wall, secant pile wall, sheet pile walls...etc</li>
    <li><span class="term">Retaining Walls:</span> including L-shaped concrete wall, gravity concrete wall, reinforced soil wall (steel strap), reinforced soil wall (geogrid), gabion wall, cantilever wall, post and panel walls ... etc</li>
    <li><span class="term">Slope Stability Analysis:</span> for low and high embankments and rock cuts as well as global stability for retaining walls</li>
    <li><span class="term">Ground Anchors Design:</span> for stressed and non-stressed anchors, screw anchors, soil nails, rock bolts, internal props...etc</li>
    <li><span class="term">General Foundation Design:</span> based on the existing investigations to ensure the existing bearing capacity withstands imposed future loads</li>
    <li><span class="term">Settlement Assessment:</span> for buildings' foundations, roads, rail, embankments on soft soils and all other geotechnical applications</li>
    <li><span class="term">Ground Improvement:</span> especially for soft soil using preloading and surcharging, wick drains, stone columns, driven concrete piles ...etc</li>
  </ul>
  <div class="visual visual--diagram" style="left:74px;top:419px" role="img" aria-label="Service symbol: shoring wall with ground anchors"></div>
  <div class="visual visual--diagram" style="left:202px;top:419px" role="img" aria-label="Service symbol: pad footing on piles"></div>
  <div class="visual visual--diagram" style="left:331px;top:419px" role="img" aria-label="Service symbol: bored pile foundation"></div>
  <div class="visual visual--diagram" style="left:74px;top:550px" role="img" aria-label="Service symbol: slope stability slip surface"></div>
  <div class="visual visual--diagram" style="left:202px;top:550px" role="img" aria-label="Service symbol: ground improvement under embankment"></div>
  <div class="visual visual--diagram" style="left:331px;top:550px" role="img" aria-label="Service symbol: gravity retaining wall"></div>
  <div class="footer-rule"></div>
  <div class="page-number">03</div>
</section>

</body>
</html>
```